Postcard Flyer For Plumbing Company

We are a p[professional plumbing company in NSW that carry out plumbing, electrical and hot water system work.
i want to send a postcard size flyer 105mm x 148mm to our clients to offer $xx off their next job they book with us.
The front of the flyer needs to say.... Feel The Love WIth $35 Off your Next Job. It needs to include a section where their name and postal address can go (74mm W x 24mm H) on the left hand side of the bottom of the flyer - refer attached example.
The other side of the flyer needs to have a section for text, the offer ($35 or $xx what they get off their next job) and also can use the tag line... Call 1 Number for The Best In 3 Trades - Plumbing, Hot Water & Electrical.
Plumbing, hot water and electrical pictures/icons can be used.
I want the flyer to stand out, use the corporate colours and be modern whilst letting them know that they can use this voucher on their next job.
Refer attachments.

Target Market(s)

Homeowners and our existing clients

Industry/Entity Type

Plumbing

Font styles to use
Serif

Colors
0255a3
ec1f27
ffffff
d3d3d3

Requirements
Must have
• Corporate colours and logos
• Red Colour:
• C=0
• M=100
• Y=100
• K=0
• Blue Colour
• C= 100
• M=66
• Y=0
• K=2
• Grey Colour
• C= 26
• M=21
• Y=19
• K=0
Nice to have
• predominately white background
Should not have
• Black background and lots of black.

```html
<!DOCTYPE html>
<html lang="en">
<head>
<meta charset="utf-8">
<title>$35 Offer Postcard</title>
<link rel="stylesheet" href="https://fonts.googleapis.com/css2?family=Montserrat:wght@300;400;700;800&family=Oswald:wght@600&display=swap">
<style>
  :root {
    --backdrop: #060808;
    --brand-red: #f20a12;
    --brand-blue: #1c4ee0;
    --panel-grey: #d5dfde;
    --gear-grey: #c6d2d1;
    --paper: #ffffff;
    --ink: #111111;
  }
  html, body {
    margin: 0;
    padding: 0;
    width: 1200px;
    height: 1200px;
    overflow: hidden;
    background: var(--backdrop);
  }
  .canvas {
    position: relative;
    width: 1200px;
    height: 1200px;
  }
  .postcard {
    position: absolute;
    left: 168px;
    top: 314px;
    width: 1065px;
    height: 755px;
    background: var(--paper);
    transform: scale(0.8);
    transform-origin: top left;
    overflow: hidden;
    font-family: "Montserrat", sans-serif;
  }
  .postcard-bands {
    position: absolute;
    inset: 0;
  }
  .offer-badge {
    position: absolute;
    left: 77px;
    top: 69px;
    width: 366px;
    height: 366px;
    border-radius: 50%;
    background: var(--brand-red);
    color: var(--paper);
    text-align: center;
  }
  .offer-amount {
    position: absolute;
    left: 0;
    right: 0;
    top: 38px;
    font-family: "Oswald", sans-serif;
    font-weight: 600;
    font-size: 200px;
    line-height: 1;
    letter-spacing: -6px;
    transform: scaleX(0.82);
  }
  .offer-label {
    position: absolute;
    left: 0;
    right: 0;
    top: 252px;
    font-weight: 300;
    font-size: 62px;
    letter-spacing: -1px;
    line-height: 1;
  }
  .pitch {
    position: absolute;
    left: 535px;
    top: 76px;
  }
  .pitch-call {
    color: var(--brand-blue);
    font-size: 70px;
    font-weight: 400;
    line-height: 68px;
    letter-spacing: -3px;
  }
  .pitch-phone {
    color: var(--brand-blue);
    font-size: 70px;
    font-weight: 800;
    line-height: 62px;
    letter-spacing: -4px;
  }
  .pitch-lead {
    color: var(--brand-blue);
    font-size: 43px;
    font-weight: 400;
    line-height: 46px;
    letter-spacing: -1.5px;
  }
  .pitch-trades {
    margin: 8px 0 0;
    color: var(--brand-red);
    font-size: 76px;
    font-weight: 800;
    line-height: 79px;
    letter-spacing: -4.5px;
  }
  .service-icons {
    position: absolute;
    left: 70px;
    top: 554px;
    display: flex;
    gap: 40px;
  }
  .service-icon {
    width: 138px;
    height: 138px;
  }
  .company-mark {
    position: absolute;
    left: 768px;
    top: 620px;
    width: 200px;
    text-align: center;
  }
  .company-name {
    color: var(--brand-blue);
    font-weight: 700;
    font-size: 22px;
    line-height: 1.1;
    letter-spacing: -0.5px;
  }
  .company-trades {
    margin-top: 10px;
    color: var(--ink);
    font-weight: 700;
    font-size: 11px;
    white-space: nowrap;
  }
</style>
</head>
<body>
<div class="canvas">
  <div class="postcard">
    <svg class="postcard-bands" viewBox="0 0 1065 755" width="1065" height="755">
      <polygon role="img" aria-label="Soft grey panel with faint pattern of interlocking gears"
        fill="var(--panel-grey)" points="0,0 1065,0 1065,458 865,548 0,410"/>
      <polygon fill="var(--brand-red)" points="0,424 838,548 1065,460 1065,466 870,557 840,566 0,444"/>
    </svg>

    <div class="offer-badge">
      <div class="offer-amount">$35</div>
      <div class="offer-label">OFFER</div>
    </div>

    <div class="pitch">
      <div class="pitch-call">Call</div>
      <div class="pitch-phone">056 0100200</div>
      <div class="pitch-lead">for the best offers in</div>
      <p class="pitch-trades">Plumbing,<br>Hot Water<br>&amp; Electrical.</p>
    </div>

    <div class="service-icons">
      <svg class="service-icon" viewBox="0 0 138 138" aria-label="Plumbing">
        <circle cx="69" cy="69" r="67" fill="none" stroke="var(--brand-red)" stroke-width="2"/>
        <g fill="var(--brand-red)">
          <rect x="28" y="48" width="26" height="14" rx="2"/>
          <rect x="54" y="40" width="20" height="28" rx="4"/>
          <rect x="58" y="28" width="12" height="12"/>
          <rect x="52" y="24" width="24" height="6" rx="2"/>
          <path d="M74 50 h20 a12 12 0 0 1 12 12 v10 h-10 v-8 a4 4 0 0 0 -4 -4 h-18z"/>
          <path d="M97 90 c-5 8 -8 12 -8 16 a8 8 0 0 0 16 0 c0 -4 -3 -8 -8 -16z"/>
        </g>
      </svg>
      <svg class="service-icon" viewBox="0 0 138 138" aria-label="Hot water">
        <circle cx="69" cy="69" r="67" fill="none" stroke="var(--brand-red)" stroke-width="2"/>
        <g fill="none" stroke="var(--brand-red)" stroke-width="3">
          <path d="M28 32 v26 h30 v-10 h20 v16 h18 v16"/>
          <path d="M38 32 v16 h30 v-10 h20 v16 h18"/>
          <path d="M84 80 h22"/>
        </g>
        <path fill="var(--brand-red)" d="M92 86 c-6 9 -9 13 -9 17 a9 9 0 0 0 18 0 c0 -4 -3 -8 -9 -17z"/>
      </svg>
      <svg class="service-icon" viewBox="0 0 138 138" aria-label="Electrical">
        <circle cx="69" cy="69" r="67" fill="none" stroke="var(--brand-red)" stroke-width="2"/>
        <g fill="none" stroke="var(--brand-red)" stroke-width="5" stroke-linecap="round">
          <path d="M52 30 l30 -6"/>
          <path d="M48 42 l40 -8"/>
          <path d="M48 54 l40 -8"/>
          <path d="M48 66 l40 -8"/>
          <path d="M50 76 l36 -6"/>
        </g>
        <rect x="52" y="84" width="34" height="18" rx="4" fill="var(--brand-red)"/>
        <path d="M58 102 h22 l-6 10 h-10z" fill="var(--brand-red)"/>
      </svg>
    </div>

    <div class="company-mark">
      <div class="company-name">Crane Contracting</div>
      <div class="company-trades">Plumbing • Electrical • Hot Water</div>
    </div>
  </div>
</div>
</body>
</html>
```